Letterhead, envelope & business card design

We would like to refresh the look and feel of our business cards & letterheads.

Our company specialises in premium property.

We are looking for a unique minimalist design for our letterhead & business cards that project this.

I can send over examples of our current design to draw from, although Im looking for some one with creativity, yet focussed on a clean modern, minimalist design.
Updates

I have just uploaded our current letterhead.

We have just removed the 'swoosh' grey symbol, but would still like to keep some part of grey in the design if possible.

thanks in advance.

Just uploaded my details for business card.

Can we see examples with the light grey used as the secondary color?

thanks in advance.

Target Market(s)

We are a premium real estate agency & we want that message to be carried through our business cards & stationery.

Industry/Entity Type

Business

```html
<!DOCTYPE html>
<html lang="en">
<head>
<meta charset="utf-8">
<title>Hargrove Estate Agents – Letterhead</title>
<link rel="stylesheet" href="https://fonts.googleapis.com/css2?family=Questrial&display=swap">
<style>
  :root {
    --teal: #1d5669;
    --grey: #a7aaae;
    --frame: #d4d6d8;
    --watermark: #d3dee3;
    --text: #4a4d50;
    --paper: #ffffff;
  }
  * { margin: 0; padding: 0; box-sizing: border-box; }
  html, body { width: 848px; height: 1200px; overflow: hidden; background: var(--paper); }
  .letterhead {
    position: relative;
    width: 848px;
    height: 1200px;
    background: var(--paper);
    font-family: "Questrial", "Century Gothic", sans-serif;
  }
  .page-frame {
    position: absolute;
    inset: 10px;
    border: 1.5px solid var(--frame);
    border-radius: 16px;
    overflow: hidden;
  }
  .corner-accent {
    position: absolute;
    left: 0;
    top: 0;
    width: 215px;
    height: 205px;
    background: radial-gradient(ellipse at top left,
      rgba(29, 86, 105, 0.55) 0%,
      rgba(167, 170, 174, 0.35) 50%,
      rgba(255, 255, 255, 0) 72%);
  }
  .brand-name {
    position: absolute;
    top: 92px;
    right: 34px;
    font-size: 26px;
    letter-spacing: 1px;
    color: var(--teal);
    text-align: right;
    line-height: 1;
    white-space: nowrap;
  }
  .watermark-name {
    position: absolute;
    left: 0;
    right: 0;
    top: 578px;
    text-align: center;
    font-size: 100px;
    letter-spacing: 4px;
    color: var(--watermark);
    line-height: 1;
  }
  .contact-footer {
    position: absolute;
    left: 0;
    right: 0;
    bottom: 4px;
    text-align: center;
    font-size: 13px;
    color: var(--text);
    line-height: 22px;
  }
  .contact-footer .item::before {
    content: "";
    display: inline-block;
    width: 8px;
    height: 8px;
    margin-right: 3px;
    border-radius: 50%;
    background: var(--teal);
    vertical-align: 0;
  }
  .contact-footer .item + .item { margin-left: 14px; }
</style>
</head>
<body>
  <main class="letterhead">
    <div class="page-frame">
      <div class="corner-accent" role="img" aria-label="Decorative curved corner accent in teal and grey"></div>

      <div class="brand-name">Hargrove Estate Agents</div>

      <div class="watermark-name" aria-hidden="true">Hargrove</div>

      <footer class="contact-footer">
        <div>
          <span class="item">Registered Valuer 052 318</span>
          <span class="item">M: 0400 555 012 &nbsp;|&nbsp; P: 02 4000 5550</span>
        </div>
        <div>
          <span class="item">18 Shore Rd, Bayview NSW 2000</span>
        </div>
      </footer>
    </div>
  </main>
</body>
</html>
```